Evergreen Touch Care Business Needs a New Website

Hello,
We require a website to be designed and coded. The design and coding must be high quality. Our website host has requested files be in static HTML format if possible.

The business is a mobile massage service for seniors (elderly people). The designer should emphasise that the business is a mobile service

The website will only have 4 pages.

1. Home- very simple layout and minimal information
2. Massage Services- this houses all of the information about the different services etc.
3. Contact Us-
4. ホーム (this is the Japanese symbol for 'home')- All of the information on the home page (section 1) will be translated into Japanese and uploaded to the brief for the designers to insert.

There is no requirement for an online booking, just contact information. The words 'Make a Booking' can be used and should lead customers to the 'Contact Us' page.

I have attached the business logo in multiple formats for designers to use.

I will upload more content and images to use for the website by the end of this week.

Thank you. I look forward to working with the successful candidate.

Target Market(s)

People aged 50+ years

Industry/Entity Type

Massage Therapy

Coding

Coded - Design and coding required

Number of Pages Required

4 page

Font styles to use
Sans Serif

Colors
74cabd
abd036
9ccb3b
f6faec
ffffff

Requirements
Must have
• Copyright free images and photos that we have taken. Both are important.
• Simple and inviting design.
Nice to have
• Colours of the logo incorporated.
Should not have
• This business is not a massage shop, so no images of massage shops or day salons required.
• Not too much imagery as the design needs to be simple.

```html
<!DOCTYPE html>
<html lang="en">
<head>
<meta charset="utf-8">
<title>Evergreen Touch Care – Mobile Massage Service</title>
<link rel="stylesheet" href="https://fonts.googleapis.com/css2?family=Cinzel:wght@400;700&family=Quicksand:wght@500;600&family=Arimo:wght@400;700&family=Great+Vibes&family=Noto+Sans+JP:wght@400&display=swap">
<style>
  :root {
    --green: #8dc63f;
    --green-deep: #7bb531;
    --green-soft: #9ccb3b;
    --lime: #abd036;
    --cream: #f6faec;
    --white: #ffffff;
    --ink: #3c3c3c;
    --body: #666666;
    --button-dark: #4a4a4a;
    --footer: #5b5b5b;
    --hero-dark: #5a4636;
    --hero-light: #b79a82;
  }
  * { box-sizing: border-box; margin: 0; padding: 0; }
  html, body { width: 1200px; height: 3232px; overflow: hidden; }
  body { position: relative; background: var(--white); font-family: "Arimo", Arial, sans-serif; color: var(--body); }
  .abs { position: absolute; }

  /* Hero */
  .hero { position: absolute; left: 0; top: 0; width: 1200px; height: 678px;
    background: linear-gradient(160deg, var(--hero-dark) 0%, #7b624d 40%, var(--hero-light) 75%, #8e735c 100%); }
  .brand { position: absolute; left: 0; width: 1200px; top: 222px; text-align: center; color: var(--lime);
    font-family: "Quicksand", sans-serif; font-weight: 500; font-size: 42px; letter-spacing: 1px; }
  .brand-sub { position: absolute; left: 350px; width: 500px; top: 270px; text-align: center; color: var(--white);
    font-family: "Quicksand", sans-serif; font-size: 16px; letter-spacing: 6px; }
  .brand-sub::before, .brand-sub::after { content: ""; position: absolute; top: 10px; width: 130px; height: 1px; background: var(--white); }
  .brand-sub::before { left: 0; } .brand-sub::after { right: 0; }
  .hero-kicker, .hero-title { position: absolute; left: 0; width: 1200px; text-align: center; color: var(--white); font-family: "Cinzel", serif; }
  .hero-kicker { top: 358px; font-size: 42px; }
  .hero-title { top: 412px; font-size: 64px; font-weight: 700; }

  .main-nav { position: absolute; left: 0; top: 614px; width: 1200px; height: 64px; border-top: 1px solid rgba(255,255,255,.35); border-bottom: 4px solid var(--green); display: flex; justify-content: center; }
  .main-nav a { display: block; height: 60px; line-height: 60px; padding: 0 26px; color: var(--white); text-decoration: none; font-family: "Quicksand", sans-serif; font-size: 16px; font-weight: 600; }
  .main-nav a.active { background: var(--green); padding: 0 28px; }
  .main-nav a.jp { font-family: "Noto Sans JP", sans-serif; font-weight: 400; }
  .nav-pointer { position: absolute; left: 590px; top: 678px; width: 0; height: 0; border-left: 10px solid transparent; border-right: 10px solid transparent; border-top: 12px solid var(--green); }

  .script { font-family: "Great Vibes", cursive; color: var(--ink); font-size: 36px; }
  .section-title { font-family: "Quicksand", sans-serif; font-weight: 500; color: var(--green); font-size: 38px; }
  .copy { font-size: 14.5px; line-height: 28px; }
  .btn { position: absolute; display: block; border-radius: 26px; text-align: center; font-family: "Quicksand", sans-serif; font-weight: 600; font-size: 15px; text-decoration: none; }

  /* Welcome */
  .welcome-script { left: 118px; width: 432px; top: 732px; text-align: center; }
  .welcome-title { left: 118px; width: 432px; top: 772px; text-align: center; }
  .welcome-copy { left: 110px; width: 448px; top: 824px; text-align: center; }
  .btn-dark { left: 258px; top: 991px; width: 148px; height: 51px; line-height: 51px; background: var(--button-dark); color: var(--white); }
  .welcome-art { left: 700px; top: 740px; width: 300px; height: 300px; border-radius: 50%; background: radial-gradient(circle, #cfe7f4 0%, #4f9ac8 55%, var(--green) 56%, var(--green-deep) 100%); }
  .welcome-art-small { left: 960px; top: 722px; width: 150px; height: 150px; border-radius: 50%; background: radial-gradient(circle, #e6d2bd 0%, #b58d6b 60%, var(--green) 61%); }

  /* Reflexology band */
  .reflex { position: absolute; left: 0; top: 1094px; width: 1200px; height: 479px; background: linear-gradient(90deg, #82bd3c 0%, var(--green-soft) 55%, #a9cf6e 100%); }
  .reflex-notch { position: absolute; left: 590px; top: 1094px; border-left: 10px solid transparent; border-right: 10px solid transparent; border-top: 12px solid var(--white); }
  .reflex-art { left: 85px; top: 1160px; width: 300px; height: 300px; border-radius: 50%; background: radial-gradient(circle, #efd8c6 0%, #c89574 62%, var(--white) 63%, var(--white) 68%, #b07d5c 69%, #b07d5c 71%, transparent 72%); }
  .reflex-title { left: 488px; top: 1152px; color: var(--white); font-family: "Quicksand", sans-serif; font-weight: 500; font-size: 38px; }
  .reflex-sub { left: 488px; top: 1204px; color: var(--white); font-family: "Quicksand", sans-serif; font-weight: 500; font-size: 28px; }
  .reflex-copy { left: 488px; top: 1256px; width: 560px; color: var(--white); }
  .btn-light { left: 487px; top: 1460px; width: 144px; height: 50px; line-height: 50px; background: var(--white); color: var(--green); }

  /* Gallery */
  .gallery-script { left: 0; width: 1200px; top: 1616px; text-align: center; }
  .gallery-title { left: 0; width: 1200px; top: 1658px; text-align: center; }
  .photo { position: absolute; }
  .p1 { left: 78px; top: 1719px; width: 249px; height: 390px; background: linear-gradient(180deg, #c9ccc4, #6f8c5a 55%, #ece8e2); }
  .p2 { left: 343px; top: 1719px; width: 514px; height: 187px; background: linear-gradient(90deg, #f2efec, #d8c2ac 50%, #eef0f2); }
  .p3 { left: 870px; top: 1719px; width: 250px; height: 390px; background: linear-gradient(180deg, #e3b899, #c4896a 60%, #8a5a40); }
  .p4 { left: 343px; top: 1921px; width: 249px; height: 390px; background: linear-gradient(180deg, #f3eeea, #d9a98b 55%, #f1e8e2); }
  .p5 { left: 607px; top: 1921px; width: 250px; height: 188px; background: linear-gradient(120deg, #cdb3a0, #e8ddd4 60%, #a48771); }
  .p6 { left: 78px; top: 2126px; width: 249px; height: 185px; background: linear-gradient(90deg, #9a9086, #d7b39a 55%, #b6aca4); }
  .p7 { left: 607px; top: 2126px; width: 513px; height: 185px; background: linear-gradient(180deg, #8f9a92, #6c8a55 45%, #e7e7e5); }

  /* Testimonial */
  .testimonial { position: absolute; left: 0; top: 2365px; width: 1200px; height: 366px; background: linear-gradient(180deg, #8cc63f 0%, #9dcb4d 70%, #86bd43 100%); }
  .testimonial-notch { position: absolute; left: 590px; top: 2731px; border-left: 10px solid transparent; border-right: 10px solid transparent; border-top: 12px solid #86bd43; }
  .quote-mark { left: 150px; top: 2398px; font-family: Georgia, serif; font-size: 110px; line-height: 1; color: rgba(255,255,255,.3); }
  .quote { left: 190px; top: 2432px; width: 460px; color: var(--white); font-size: 15px; line-height: 26px; }
  .quote-name { left: 190px; top: 2628px; color: var(--white); font-family: "Quicksand", sans-serif; font-weight: 600; font-size: 19px; }
  .polaroid { left: 717px; top: 2428px; width: 216px; height: 265px; background: var(--white); padding: 14px 14px 56px; box-shadow: 0 4px 12px rgba(0,0,0,.2); }
  .polaroid-photo { width: 100%; height: 100%; background: linear-gradient(135deg, #e6c23a 0%, #c8503a 45%, #5a8ac0 100%); }

  /* Why */
  .why-script { left: 0; width: 1200px; top: 2776px; text-align: center; }
  .why-title { left: 0; width: 1200px; top: 2814px; text-align: center; }
  .pill { position: absolute; height: 48px; border: 2px solid #e3e3e3; border-radius: 24px; background: var(--white); display: flex; align-items: center; padding-left: 14px; gap: 12px; font-size: 13.5px; color: var(--body); }
  .pill svg { flex: none; }

  /* Footer */
  .site-footer { position: absolute; left: 0; top: 3063px; width: 1200px; height: 169px; background: var(--footer); }
  .footer-nav { position: absolute; left: 80px; top: 3096px; display: flex; gap: 44px; font-size: 14px; }
  .footer-nav a { color: var(--white); text-decoration: none; }
  .footer-nav a.active { color: var(--green); }
  .footer-brand { left: 0; width: 1200px; top: 3108px; text-align: center; color: var(--green); font-family: "Quicksand", sans-serif; font-weight: 600; font-size: 17px; }
  .footer-rule { left: 80px; top: 3158px; width: 1040px; height: 1px; background: rgba(255,255,255,.25); }
  .social { position: absolute; top: 3086px; width: 42px; height: 42px; border-radius: 50%; border: 2px solid var(--white); }
  .social.active { background: var(--green); border-color: var(--green); }
  .copyright { left: 0; width: 1200px; top: 3194px; text-align: center; color: var(--white); font-size: 13px; }
  .copyright span { color: var(--green); }
</style>
</head>
<body>

<header class="hero" role="img" aria-label="Photo of a smiling senior woman relaxing during a back massage"></header>
<div class="brand">EVERGREEN TOUCH CARE</div>
<div class="brand-sub">AUSTRALIA</div>
<h1 class="hero-kicker">We are Astralia based</h1>
<div class="hero-title">Mobile Massage Service</div>

<nav class="main-nav">
  <a class="active" href="#">HOME</a>
  <a href="#">MESSAGE SERVICES</a>
  <a href="#">CONTACT US</a>
  <a class="jp" href="#">ホーム</a>
</nav>
<div class="nav-pointer"></div>

<section>
  <div class="abs script welcome-script">Welcome to</div>
  <h2 class="abs section-title welcome-title">Evergreen Touch Care</h2>
  <p class="abs copy welcome-copy">Lorem Ipsum is simply dummy text of the printing and typesetting industry. Lorem Ipsum has been the industry's standard dummy text ever since the 1500s, when an unknown printer took a galley of type and scrambled it to make a type specimen book. It has survived not only five centuries, but also the leap into electronic typesetting, remaining essentially unchanged.</p>
  <a class="btn btn-dark" href="#">READ MORE</a>
  <div class="abs welcome-art" role="img" aria-label="Image of a white lotus flower on blue water in a green frame"></div>
  <div class="abs welcome-art-small" role="img" aria-label="Image of massage stones and towels in a small green frame"></div>
</section>

<section class="reflex" role="img" aria-label="Soft green-tinted photo of a smiling senior woman"></section>
<div class="reflex-notch"></div>
<div class="abs reflex-art" role="img" aria-label="Photo of hands giving a foot reflexology massage"></div>
<h2 class="abs reflex-title">Reflexology</h2>
<div class="abs reflex-sub">We relieve tension and treat illness</div>
<p class="abs copy reflex-copy">Lorem Ipsum is simply dummy text of the printing and typesetting industry. Lorem Ipsum has been the industry's standard dummy text ever since the 1500s, when an unknown printer took a galley of type and scrambled it to make a type specimen book. It has survived not only five centuries, but also the leap into electronic typesetting, remaining essentially unchanged. It was popularised in the 1960s with the release of Letraset sheets containing Lorem Ipsum passages.</p>
<a class="btn btn-light" href="#">READ MORE</a>

<section>
  <div class="abs script gallery-script">Check Out</div>
  <h2 class="abs section-title gallery-title">Our Gallery</h2>
  <div class="photo p1" role="img" aria-label="Therapist giving a back massage outdoors on a lawn"></div>
  <div class="photo p2" role="img" aria-label="Senior woman lying down receiving a shoulder massage"></div>
  <div class="photo p3" role="img" aria-label="Close view of a foot massage"></div>
  <div class="photo p4" role="img" aria-label="Close view of hands massaging a shoulder"></div>
  <div class="photo p5" role="img" aria-label="Senior man receiving a back massage"></div>
  <div class="photo p6" role="img" aria-label="Hands massaging a calf"></div>
  <div class="photo p7" role="img" aria-label="Back massage on a table outdoors by a lawn"></div>
</section>

<section class="testimonial" role="img" aria-label="Soft green background with a blurred lawn"></section>
<div class="testimonial-notch"></div>
<div class="abs quote-mark">&ldquo;</div>
<blockquote class="abs quote">"Lorem Ipsum is simply dummy text of the printing and typesetting industry. Lorem Ipsum has been the industry's standard dummy text ever since the 1500s, when an unknown printer took a galley of type and scrambled it to make a type specimen book. It has survived not only five centuries, but also the leap into electronic typesetting, remaining essentially unchanged."</blockquote>
<div class="abs quote-name">MAREN HOLT</div>
<div class="abs polaroid"><div class="polaroid-photo" role="img" aria-label="Instant photo of a happy couple in warm winter clothes"></div></div>

<section>
  <div class="abs script why-script">Why</div>
  <h2 class="abs section-title why-title">Evergreen Touch Care</h2>
  <div class="pill" style="left:205px;top:2900px;width:385px;"><svg width="22" height="22" viewBox="0 0 22 22"><circle cx="11" cy="11" r="11" fill="#8dc63f"/><path d="M6 11.5l3.3 3.2L16 8" stroke="#fff" stroke-width="2.4" fill="none" stroke-linecap="round" stroke-linejoin="round"/></svg>We give hassle Free Mobile Massage Services</div>
  <div class="pill" style="left:601px;top:2900px;width:185px;"><svg width="22" height="22" viewBox="0 0 22 22"><circle cx="11" cy="11" r="11" fill="#8dc63f"/><path d="M6 11.5l3.3 3.2L16 8" stroke="#fff" stroke-width="2.4" fill="none" stroke-linecap="round" stroke-linejoin="round"/></svg>We are Panctual</div>
  <div class="pill" style="left:797px;top:2900px;width:198px;"><svg width="22" height="22" viewBox="0 0 22 22"><circle cx="11" cy="11" r="11" fill="#8dc63f"/><path d="M6 11.5l3.3 3.2L16 8" stroke="#fff" stroke-width="2.4" fill="none" stroke-linecap="round" stroke-linejoin="round"/></svg>We are Passionate</div>
  <div class="pill" style="left:205px;top:2962px;width:288px;"><svg width="22" height="22" viewBox="0 0 22 22"><circle cx="11" cy="11" r="11" fill="#8dc63f"/><path d="M6 11.5l3.3 3.2L16 8" stroke="#fff" stroke-width="2.4" fill="none" stroke-linecap="round" stroke-linejoin="round"/></svg>We are Trained &amp; well Qualified</div>
  <div class="pill" style="left:506px;top:2962px;width:261px;"><svg width="22" height="22" viewBox="0 0 22 22"><circle cx="11" cy="11" r="11" fill="#8dc63f"/><path d="M6 11.5l3.3 3.2L16 8" stroke="#fff" stroke-width="2.4" fill="none" stroke-linecap="round" stroke-linejoin="round"/></svg>We Charge Resonable rate</div>
</section>

<footer class="site-footer"></footer>
<nav class="footer-nav">
  <a class="active" href="#">Home</a>
  <a href="#">Massage Services</a>
  <a href="#">Contact</a>
</nav>
<div class="abs footer-brand">EVERGREEN TOUCH CARE</div>
<div class="abs footer-rule"></div>
<a class="social active" href="#" style="left:927px;" aria-label="Social link"></a>
<a class="social" href="#" style="left:976px;" aria-label="Social link"></a>
<a class="social" href="#" style="left:1028px;" aria-label="Social link"></a>
<a class="social" href="#" style="left:1079px;" aria-label="Social link"></a>
<div class="abs copyright">© <span>EVERGREEN TOUCH CARE</span> – 2016. All Rights Reserved.</div>

</body>
</html>
```